Property risk and finance brokerage company needs a business card design

Tarlow Financial requires a business card design. Please integrate existing logo (refer uploaded file).
hex codes used on logo #002649 #008ED6 #444F51 #ADAFAA
font used - Cinzel
Contact information
Renata Sollisford
Director
Mobile: 0491 738 205
email: r.sollisford@tarlowfinancial.example.au
website: www.tarlowfinancial.example.au
CRN : 918354
PO Box 527
Ellmont, Victoria, 3178
Horizontal orientation please
Finance

```html
<!DOCTYPE html>
<html lang="en">
<head>
<meta charset="utf-8">
<title>Tarlow Financial — Business Card</title>
<link rel="stylesheet" href="https://fonts.googleapis.com/css2?family=Cinzel:wght@400&family=Montserrat:wght@400;500&display=swap">
<style>
  :root {
    --navy: #002649;
    --blue-deep: #0b4a8a;
    --blue: #008ED6;
    --blue-text: #0a5aa6;
    --slate: #444F51;
    --stone: #ADAFAA;
    --paper: #ffffff;
    --ground: #b9bcbf;
    --ghost: #ececec;
  }
  * { margin: 0; padding: 0; box-sizing: border-box; }
  html, body { width: 1200px; height: 900px; overflow: hidden; }
  body {
    background: var(--ground);
    display: flex;
    flex-direction: column;
    align-items: center;
    justify-content: center;
    gap: 56px;
    font-family: "Montserrat", sans-serif;
  }
  .card {
    position: relative;
    width: 560px;
    height: 320px;
    border-radius: 26px;
    overflow: hidden;
    box-shadow: 0 10px 24px rgba(0,0,0,0.18);
  }

  /* Front */
  .card--front {
    background: linear-gradient(150deg, var(--blue-deep) 0%, #063a70 50%, var(--navy) 100%);
    color: var(--paper);
  }
  .card--front .decor {
    position: absolute;
    left: -40px; top: -30px;
    width: 360px; height: 380px;
    border-radius: 50%;
    background: radial-gradient(circle, rgba(0,38,73,0.45) 0%, rgba(0,38,73,0) 70%);
  }
  .front-brand {
    position: absolute;
    left: 0; right: 0; top: 118px;
    display: flex;
    flex-direction: column;
    align-items: center;
    gap: 18px;
  }
  .brand {
    display: flex;
    align-items: center;
    gap: 14px;
    font-family: "Cinzel", serif;
    font-weight: 400;
    letter-spacing: 0.04em;
    white-space: nowrap;
  }
  .brand__dot { border-radius: 50%; flex: none; }
  .card--front .brand { font-size: 40px; color: var(--paper); }
  .card--front .brand__dot { width: 34px; height: 34px; background: var(--paper); }
  .front-web { font-size: 13px; letter-spacing: 0.03em; color: #dfe8f2; }

  /* Back */
  .card--back { background: var(--paper); }
  .card--back .decor {
    position: absolute;
    left: 20px; top: 40px;
    width: 300px; height: 300px;
    border-radius: 46% 54% 40% 60%;
    background: radial-gradient(circle at 50% 40%, var(--ghost) 0%, rgba(236,236,236,0.4) 60%, rgba(236,236,236,0) 80%);
  }
  .back-info {
    position: absolute;
    right: 40px; top: 34px;
    width: 300px;
    display: flex;
    flex-direction: column;
    align-items: flex-end;
    text-align: right;
    color: var(--slate);
  }
  .card--back .brand { font-size: 25px; color: var(--navy); gap: 10px; }
  .card--back .brand__dot { width: 24px; height: 24px; background: var(--blue); }
  .rule { width: 190px; height: 1px; background: var(--stone); margin: 14px 0 14px; }
  .person__name { font-size: 21px; color: var(--blue-text); font-weight: 500; line-height: 1.1; }
  .person__role { font-size: 12px; margin-bottom: 16px; }
  .line { font-size: 12px; line-height: 1.45; display: flex; align-items: center; gap: 6px; justify-content: flex-end; }
  .gap { margin-top: 14px; }
  .icon { width: 11px; height: 11px; flex: none; }
  .crn { color: var(--blue-text); }
</style>
</head>
<body>
  <section class="card card--front" aria-label="Card front">
    <div class="decor" role="img" aria-label="Faint large leaf decoration in darker blue"></div>
    <div class="front-brand">
      <div class="brand"><span class="brand__dot"></span>Tarlow Financial</div>
      <p class="front-web">www.tarlowfinancial.example.au</p>
    </div>
  </section>

  <section class="card card--back" aria-label="Card back">
    <div class="decor" role="img" aria-label="Faint large leaf decoration in light grey"></div>
    <div class="back-info">
      <div class="brand"><span class="brand__dot"></span>Tarlow Financial</div>
      <div class="rule"></div>
      <p class="person__name">Renata Sollisford</p>
      <p class="person__role">Managing Director</p>
      <p class="line">PO Box 527</p>
      <p class="line">Ellmont, Victoria, 3178</p>
      <p class="line gap">0491 738 205
        <svg class="icon" viewBox="0 0 12 12" aria-hidden="true"><rect width="12" height="12" rx="2" fill="#002649"/><path d="M3.5 2.8l1.3 0 .6 1.6-.8.6a5 5 0 002.4 2.4l.6-.8 1.6.6v1.3c-3.2.3-6-2.5-5.7-5.7z" fill="#fff"/></svg>
      </p>
      <p class="line">r.sollisford@tarlowfinancial.example.au
        <svg class="icon" viewBox="0 0 12 12" aria-hidden="true"><rect width="12" height="12" rx="2" fill="#008ED6"/><rect x="2.5" y="3.5" width="7" height="5" fill="none" stroke="#fff" stroke-width="1"/><path d="M2.5 3.5l3.5 3 3.5-3" fill="none" stroke="#fff" stroke-width="1"/></svg>
      </p>
      <p class="line crn">Credit Rep No: nnn nnn nnn</p>
    </div>
  </section>
</body>
</html>
```